Tidal Spoon is a modern and professional services business in the field of hospitality.

Need business card for a professional chef and consultant. Attention to detail and to stand out is our goal. I want a professional and stand out card which is not generic.
Would like a modern card with black gold or blue I’m not very sure on colours yet , open to ideas from those in the know. This is my second project and have been really happy with the process so far.
With 15 years in the hospitality industry I am launching into consulting and starting my own business. I’d like a few types of designs to look at which style I want. Open to suggestions. Thanks in advance for the work. I want something that will become part of my brand as it is launched. There is a chance for possible future work to the right person.

Target Market(s)

Restauranters and Registered training organisations.

Industry/Entity Type

Professional Service

Font styles to use
Serif

Colors

Designer to choose colors to be used in the design.

Requirements
Must have
• A stand out design, blue / black
Nice to have
• Can u get embossed cards?
Should not have
• Na

```html
<!DOCTYPE html>
<html lang="en">
<head>
<meta charset="utf-8">
<title>Tidal Spoon — Business Card</title>
<link rel="stylesheet" href="https://fonts.googleapis.com/css2?family=Libre+Baskerville:wght@400;700&display=swap">
<style>
  :root {
    --backdrop: #e9e6e1;
    --card-black: #0b0b0c;
    --card-edge: #1c1c1e;
    --brand-blue: #1ba3e2;
    --frame-glow: rgba(27, 163, 226, 0.55);
    --text-white: #f2f2f2;
    --text-grey: #bdbdbd;
    --utensil-tone: #d9d9d9;
  }
  * { margin: 0; padding: 0; box-sizing: border-box; }
  html, body {
    width: 1200px;
    height: 900px;
    overflow: hidden;
    background: var(--backdrop);
  }
  .canvas {
    position: relative;
    width: 1200px;
    height: 900px;
    font-family: "Libre Baskerville", Georgia, serif;
  }
  .business-card {
    position: absolute;
    left: 100px;
    top: 170px;
    width: 1000px;
    height: 560px;
    background: radial-gradient(ellipse at 60% 35%, var(--card-edge), var(--card-black) 70%);
    box-shadow: 0 18px 40px rgba(0, 0, 0, 0.35);
  }
  .card-frame {
    position: absolute;
    inset: 36px;
    border: 3px solid var(--brand-blue);
    box-shadow: 0 0 10px var(--frame-glow), inset 0 0 10px var(--frame-glow);
  }
  .brand-mark {
    position: absolute;
    left: 120px;
    top: 95px;
    display: flex;
    align-items: center;
    gap: 22px;
  }
  .brand-dot {
    width: 58px;
    height: 58px;
    border-radius: 50%;
    background: var(--text-white);
  }
  .brand-name {
    font-size: 92px;
    font-weight: 700;
    color: var(--brand-blue);
    line-height: 1;
    letter-spacing: 1px;
    white-space: nowrap;
  }
  .identity {
    position: absolute;
    right: 545px;
    top: 292px;
    text-align: right;
  }
  .person-name {
    font-size: 30px;
    font-weight: 700;
    color: var(--brand-blue);
    margin-bottom: 10px;
  }
  .person-role,
  .person-address {
    font-size: 21px;
    color: var(--text-grey);
    line-height: 1.45;
  }
  .person-role { margin-bottom: 14px; }
  .utensil-fill {
    position: absolute;
    left: 478px;
    top: 258px;
    width: 34px;
    height: 210px;
    border-radius: 17px 17px 12px 12px;
    background: linear-gradient(180deg, var(--utensil-tone), #8a8a8a);
  }
  .contact-list {
    position: absolute;
    left: 548px;
    top: 262px;
    list-style: none;
  }
  .contact-item {
    display: flex;
    align-items: center;
    gap: 16px;
    font-size: 21px;
    color: var(--text-white);
    height: 38px;
  }
  .contact-icon {
    width: 22px;
    height: 22px;
    flex: none;
    fill: var(--brand-blue);
    stroke: var(--brand-blue);
  }
</style>
</head>
<body>
<main class="canvas">
  <section class="business-card">
    <div class="card-frame"></div>

    <div class="brand-mark">
      <span class="brand-dot"></span>
      <span class="brand-name">Tidal Spoon</span>
    </div>

    <div class="identity">
      <p class="person-name">Your Name</p>
      <p class="person-role">Managing Member</p>
      <p class="person-address">27 Harbour Lane,<br>Seaview, CA 90210</p>
    </div>

    <div class="utensil-fill" role="img" aria-label="Illustration of a silver fork"></div>

    <ul class="contact-list">
      <li class="contact-item">
        <svg class="contact-icon" viewBox="0 0 22 22" aria-hidden="true"><rect x="5" y="1.5" width="12" height="19" rx="2" fill="none" stroke-width="2"/><rect x="7.5" y="4.5" width="7" height="10" stroke="none"/></svg>
        (555) 210-4476
      </li>
      <li class="contact-item">
        <svg class="contact-icon" viewBox="0 0 22 22" aria-hidden="true"><rect x="6" y="2" width="10" height="6" stroke="none"/><rect x="2" y="8" width="18" height="8" rx="2" stroke="none"/><rect x="6" y="14" width="10" height="6" fill="#0b0b0c" stroke-width="2"/></svg>
        (555) 210-4477
      </li>
      <li class="contact-item">
        <svg class="contact-icon" viewBox="0 0 22 22" aria-hidden="true"><rect x="2" y="5" width="18" height="12" stroke="none"/><path d="M2 5 L11 12 L20 5" fill="none" stroke="#0b0b0c" stroke-width="1.6"/></svg>
        hello@tidalspoon.com
      </li>
      <li class="contact-item">
        <svg class="contact-icon" viewBox="0 0 22 22" aria-hidden="true"><circle cx="11" cy="11" r="9" stroke="none"/><path d="M2 11 H20 M11 2 C6 7 6 15 11 20 M11 2 C16 7 16 15 11 20" fill="none" stroke="#0b0b0c" stroke-width="1.3"/></svg>
        www.tidalspoon.com
      </li>
    </ul>
  </section>
</main>
</body>
</html>
```